Employee engagement survey desk drop

We want to get employees excited about the upcoming employee engagement survey so as part of our campaign we will be doing a desk drop/flyer. The final print size is 5.5" tall x 8.5" wide so need the final layout to be 2-up on an 8.5 x 11 (letter-size) paper. Other specs: one-sided, 4-color. The theme is "engagement" and this piece will accompany a candy "glim drop" (think engagement ring).
Updates

Following is proposed content for the piece. Feel free to edit the body copy to fit the design theme, if needed. BODY COPY: Corvessa is deeply committed to our employees and we want to take this relationship to the next level. Therefore, it’s time for a proper proposal: will you, Corvessa employee, take the annual employee engagement survey? We want to understand your feelings, experiences, and ideas for ways to ways to strengthen and fortify our relationship. ADDITIONAL DETAILS: You will receive an email on June 6, 2018 with a link to the employee engagement survey. Please complete the survey by June 26, 2018.

Target Market(s)

Employees

Requirements
Must have
• 1.) Should mention "Corvessa Employee Engagement Survey"
• 2.) The logo provided should be a smaller element in the overall design.
Nice to have
• 1.) I've attached our brand guidelines with color and font details. It's not necessary to use only the colors available in our palette but where you do use these colors, please refer to this document. For example, if you are using red, use CMYK 3-100-59-12.
• 2.) You do not have to use the fonts outlined in the brand guidelines, if they don't match the design. Feel free to use more romantic fonts (decorative or script) if they fit better.
• 3.) Corvessa is a hearing health/hearing aid company whose tagline is "bringing sound to life" so any ideas that could incorporate that theme as well as the ring would be cool.

```html
<!DOCTYPE html>
<html lang="en">
<head>
<meta charset="utf-8">
<title>Corvessa Employee Engagement Survey – Desk Drop</title>
<link rel="stylesheet" href="https://fonts.googleapis.com/css2?family=Carlito:wght@400;700&family=Cinzel:wght@500;600&display=swap">
<style>
  :root {
    --brand-red: #be1045;
    --ink: #1c1c1c;
    --photo-dark: #4e4e4e;
    --photo-mid: #7d7d7d;
    --photo-light: #b4b4b4;
    --panel: rgba(236, 236, 236, 0.8);
    --ornament: rgba(255, 255, 255, 0.5);
    --paper: #ffffff;
  }
  * { box-sizing: border-box; margin: 0; padding: 0; }
  html, body { width: 864px; height: 1200px; overflow: hidden; }
  body { font-family: "Carlito", "Calibri", sans-serif; color: var(--ink); }

  .flyer { position: relative; width: 864px; height: 1200px; overflow: hidden; }

  .flyer__photo {
    position: absolute; inset: 0;
    background:
      radial-gradient(ellipse 40% 60% at 55% 35%, var(--photo-light), transparent 70%),
      linear-gradient(135deg, var(--photo-mid) 0%, var(--photo-dark) 55%, var(--photo-mid) 100%);
  }

  .brand-box {
    position: absolute; left: 225px; top: 53px; width: 376px; height: 153px;
    background: var(--paper);
    display: flex; align-items: center; justify-content: center;
  }
  .brand-box__name { font-size: 40px; font-weight: 700; color: var(--brand-red); }

  .panel { position: absolute; left: 0; top: 0; width: 864px; height: 1200px; }

  .ornament { position: absolute; background: var(--ornament); }
  .ornament--top-left { left: 98px; top: 326px; width: 252px; height: 205px; }
  .ornament--bottom-right { left: 486px; top: 930px; width: 280px; height: 194px; }

  .message {
    position: absolute; left: 162px; top: 556px; width: 540px;
    text-align: center;
  }
  .message__body { font-size: 21.5px; line-height: 27px; padding: 0 6px; }
  .message__detail { font-size: 26px; line-height: 30px; }
  .message__detail--first { margin-top: 35px; }
  .message__date {
    font-family: "Cinzel", "Trajan Pro", serif; font-weight: 600;
    font-size: 37px; line-height: 40px; color: var(--brand-red);
  }

  .divider { display: flex; align-items: center; justify-content: center; margin: 12px auto 6px; width: 440px; }
  .divider__line { flex: 1; height: 1.5px; background: var(--brand-red); }
  .divider__flourish { width: 96px; height: 10px; background: var(--brand-red); border-radius: 5px; }
</style>
</head>
<body>
  <main class="flyer">
    <div class="flyer__photo" role="img" aria-label="Soft-focus black and white close-up photo of a glim drop ring candy"></div>

    <header class="brand-box">
      <span class="brand-box__name">Corvessa</span>
    </header>

    <svg class="panel" width="864" height="1200" viewBox="0 0 864 1200" aria-hidden="true">
      <path d="M98 326 H766 V1124 H300 C180 1124 98 1000 98 818 Z" fill="var(--panel)"/>
    </svg>

    <div class="ornament ornament--top-left" role="img" aria-label="White floral filigree corner ornament"></div>
    <div class="ornament ornament--bottom-right" role="img" aria-label="White floral filigree corner ornament"></div>

    <section class="message">
      <p class="message__body">Corvessa is deeply committed to our employees and we want to take this relationship to the next level. Therefore, it’s time for a proper proposal: will you, Corvessa employee, take the annual employee engagement survey? We want to understand your feelings, experiences, and ideas for ways to ways to strengthen and fortify our relationship.</p>

      <p class="message__detail message__detail--first">You will receive an email on</p>
      <p class="message__date">June 6, 2018</p>
      <p class="message__detail">with a link to the employee engagement survey.</p>

      <div class="divider">
        <span class="divider__line"></span>
        <span class="divider__flourish" role="img" aria-label="Small red scroll flourish"></span>
        <span class="divider__line"></span>
      </div>

      <p class="message__detail">Please complete the survey by</p>
      <p class="message__date">June 26, 2018.</p>
    </section>
  </main>
</body>
</html>
```